Menu Design Project

My Restaurant is called The Pita Corner, it's fast food restaurant serves Gyro, Wings, Subs, Fried Seafood and chicken tenders. I'm looking for a menu design to fit the fast food category and have some photos of the food on the front page as well inside the menu. I will attached some photos and you can add any other photo related to the menu from the web.

Industry/Entity Type

Restaurant

```html
<!DOCTYPE html>
<html lang="en">
<head>
<meta charset="utf-8">
<title>The Pita Corner – Menu</title>
<link href="https://fonts.googleapis.com/css2?family=Montserrat:wght@500;700&family=Open+Sans:ital,wght@0,400;0,600;1,400&family=Oswald:wght@400;700&family=Great+Vibes&family=Michroma&display=swap" rel="stylesheet">
<style>
:root{
  --red:#e8141b;
  --red-dark:#c40d13;
  --black:#0d0d0d;
  --white:#ffffff;
  --ink:#1a1a1a;
  --stage:#e9e9e9;
}
*{box-sizing:border-box;margin:0;padding:0}
html,body{width:1200px;height:770px;overflow:hidden;background:var(--stage)}
body{position:relative;font-family:"Open Sans",sans-serif;color:var(--ink)}
.sheet{position:absolute;top:25px;width:560px;height:720px;box-shadow:0 4px 14px rgba(0,0,0,.18)}
.sheet--outside{left:30px}
.sheet--inside{left:610px}
.panel{position:absolute;left:0;width:560px;height:360px;background:var(--red);padding:14px}
.panel--top{top:0}
.panel--bottom{top:360px;border-top:1px solid var(--red-dark)}
.panel__inner{position:relative;width:100%;height:100%;background:var(--white);overflow:hidden}
.placeholder{position:absolute;border-radius:6px}
.checker{position:absolute;width:110px;height:70px;background:linear-gradient(135deg,#f28a8d,#e8141b)}
.checker--tl{left:0;top:0;clip-path:polygon(0 0,100% 0,0 100%)}
.checker--tr{right:0;top:0;clip-path:polygon(0 0,100% 0,100% 100%)}
.brand-mark{display:block;width:34px;height:34px;border-radius:50%;background:var(--red);margin:0 auto}
.section-tag{position:absolute;display:flex;align-items:center;gap:8px;background:var(--black);color:var(--white);
  font-family:"Michroma",sans-serif;font-size:10.5px;letter-spacing:.5px;height:18px;padding:0 12px 0 6px;border-radius:0 9px 9px 0;white-space:nowrap}
.section-tag::before{content:"";width:8px;height:8px;border-radius:50%;background:var(--white);box-shadow:inset 0 0 0 2px var(--red)}
.price-list{position:absolute;list-style:none;font-size:10.5px;line-height:15.5px}
.price-list li{display:flex;justify-content:space-between;gap:10px;white-space:nowrap}
.price-list .note{color:var(--red)}
.script{font-family:"Great Vibes",cursive}

/* outside back */
.band{position:absolute;left:0;right:0;top:0;height:34px;background:var(--black);color:var(--white);
  display:flex;align-items:center;padding-left:24px;font-size:22px}
.drinks{position:absolute;left:24px;top:52px;width:200px}
.drinks .section-tag{position:static;display:inline-flex;margin-bottom:8px}
.drinks p{font-size:11px;line-height:16px}
.drink-cans{position:absolute;left:200px;top:60px;width:110px;height:120px}
.map{left:330px;top:48px;width:190px;height:140px;background:linear-gradient(135deg,#dfe1e4,#c9ccd1);border:2px solid #b9bcc2}
.call{position:absolute;left:24px;top:200px;width:280px;font-size:11px}
.call strong{display:block;color:var(--red);font-family:"Oswald",sans-serif;font-size:15px;margin-top:2px}
.hours-small{position:absolute;left:330px;top:208px;font-size:11px}
.hours-small strong{display:block;color:var(--red);font-family:"Oswald",sans-serif;font-size:15px}
.address-line{position:absolute;left:24px;right:24px;bottom:14px;border-top:1px solid #666;padding-top:6px;font-size:11px;display:flex;gap:14px}

/* cover */
.cover__logo{position:absolute;left:0;right:0;top:16px}
.cover__name{position:absolute;left:0;right:0;top:58px;text-align:center;font-family:"Montserrat",sans-serif;font-weight:700;font-size:16px}
.cover__title{position:absolute;left:0;right:0;top:80px;text-align:center;font-size:58px;color:var(--red);line-height:70px}
.cover__rule{position:absolute;left:190px;width:150px;height:1px;background:var(--red);top:152px}
.cutlery{top:86px;width:80px;height:80px;background:radial-gradient(circle,#e9d7b0,#c9c9c9);border-radius:50%}
.food{top:190px;width:100px;height:70px;background:linear-gradient(135deg,#c97a3a,#7a3a14)}
.cover__hours{position:absolute;left:0;right:0;top:270px;text-align:center;font-family:"Oswald",sans-serif;font-size:16px}
.cover__hours strong{color:var(--red)}
.cover__footer{position:absolute;left:0;right:0;bottom:0;height:28px;background:var(--black);color:var(--white);
  display:flex;align-items:center;justify-content:center;gap:18px;font-size:12.5px}
.cover__footer svg{width:11px;height:11px;vertical-align:-1px;margin-right:5px}

/* inside */
.inside__head{position:absolute;left:0;right:0;top:10px;text-align:center}
.inside__head h1{font-family:"Montserrat",sans-serif;font-weight:700;font-size:13px;margin-top:4px}
.kids{position:absolute;left:138px;top:218px;width:256px;text-align:center;font-size:10px;line-height:15px}
.kids .section-tag{position:static;display:inline-flex;margin-bottom:6px;border-radius:9px}
.kids ul{text-align:left}
.kids li{list-style:none;display:flex;justify-content:space-between;gap:8px;white-space:nowrap}
.kids b{color:var(--red)}
.meal-photo{top:215px;width:118px;height:110px;background:linear-gradient(135deg,#f2c14e,#d9301f)}
.cheese{color:var(--red);font-size:8px}
</style>
</head>
<body>

<section class="sheet sheet--outside">
  <div class="panel panel--top">
    <div class="panel__inner">
      <div class="band script">Good Food, Good Mood</div>
      <div class="drinks">
        <span class="section-tag">DRINKS</span>
        <p>Cola, Diet Cola,<br>Lemon-Lime, Sports Drink,<br>Strawberry Soda,<br>Orange Soda,<br>Pepper Soda and more.</p>
      </div>
      <div class="placeholder drink-cans" role="img" aria-label="Photo of assorted soda cans" style="background:linear-gradient(135deg,#f0a24a,#c8102e 55%,#3f8f3a)"></div>
      <div class="placeholder map" role="img" aria-label="Street map showing the restaurant location"></div>
      <div class="call">Call Us for Pick Up orders or Catering<strong>713-555-0148</strong></div>
      <div class="hours-small">Hours of operation:<strong>Monday to Sunday 11am-9pm</strong></div>
      <div class="address-line"><span>4810 Cedar Grove Ave, Houston, TX 77021</span><span>713-555-0148</span></div>
    </div>
  </div>
  <div class="panel panel--bottom">
    <div class="panel__inner">
      <div class="checker checker--tr" role="img" aria-label="Red and white checkered corner"></div>
      <div class="cover__logo"><span class="brand-mark"></span></div>
      <div class="cover__name">The Pita Corner Restaurant</div>
      <div class="cover__title script">Menu</div>
      <div class="cover__rule"></div>
      <div class="placeholder cutlery" style="left:40px" role="img" aria-label="Fork, spoon and knife tied with a gold bow"></div>
      <div class="placeholder cutlery" style="right:40px" role="img" aria-label="Fork, spoon and knife tied with a gold bow"></div>
      <div class="placeholder food" style="left:75px" role="img" aria-label="Photo of chicken wings"></div>
      <div class="placeholder food" style="left:216px;background:linear-gradient(135deg,#d99a4a,#6b8f2a 50%,#8a3a1a)" role="img" aria-label="Photo of a burger"></div>
      <div class="placeholder food" style="left:357px;background:linear-gradient(135deg,#eed9a8,#8a5a34)" role="img" aria-label="Photo of a gyro wrap"></div>
      <div class="cover__hours">Hours of operation: <strong>Monday to Sunday 11am-9pm</strong></div>
      <div class="cover__footer">
        <span><svg viewBox="0 0 12 12"><path d="M6 0a4 4 0 0 0-4 4c0 3 4 8 4 8s4-5 4-8a4 4 0 0 0-4-4zm0 5.5A1.5 1.5 0 1 1 6 2.5a1.5 1.5 0 0 1 0 3z" fill="#fff"/></svg>4810 Cedar Grove Ave, Houston, TX 77021</span>
        <span><svg viewBox="0 0 12 12"><path d="M2.5 1l2 2-1 1.5c.8 1.6 2 2.8 3.5 3.5L8.5 7l2 2-1.5 2C5 10.5 1.5 7 1 3z" fill="#fff"/></svg>713-555-0148</span>
      </div>
    </div>
  </div>
</section>

<section class="sheet sheet--inside">
  <div class="panel panel--top">
    <div class="panel__inner">
      <div class="checker checker--tl" role="img" aria-label="Red and white checkered corner"></div>
      <div class="checker checker--tr" role="img" aria-label="Red and white checkered corner"></div>
      <div class="inside__head"><span class="brand-mark" style="width:28px;height:28px"></span><h1>The Pita Corner Menu</h1></div>

      <span class="section-tag" style="left:0;top:80px">CHICKEN</span>
      <ul class="price-list" style="left:18px;top:102px;width:200px">
        <li><span>10 Large Wings</span><span>$8.99</span></li>
        <li><span>20 Large Wings</span><span>$16.99</span></li>
        <li><span>30 Large Wings</span><span>$23.99</span></li>
        <li><span>50 Large Wings</span><span>$39.99</span></li>
        <li><span>½ lb. Chicken Strips</span><span>$5.49</span></li>
        <li><span>1lb. Chicken Strips</span><span>$7.99</span></li>
        <li><span>½ lb. Gizzards</span><span>$5.49</span></li>
        <li><span>1lb. Gizzards</span><span>$7.99</span></li>
      </ul>
      <span class="section-tag" style="left:0;top:232px">SEAFOOD</span>
      <ul class="price-list" style="left:18px;top:254px;width:200px">
        <li><span>½ lb. Shrimp</span><span>$7.99</span></li>
        <li><span>1lb. Shrimp</span><span>$13.99</span></li>
        <li><span>½ lb. Fish</span><span>$6.99</span></li>
        <li><span>1lb. Fish</span><span>$12.99</span></li>
      </ul>

      <span class="section-tag" style="right:0;top:80px;border-radius:9px 0 0 9px">FRESH SALAD</span>
      <ul class="price-list" style="left:250px;top:102px;width:262px">
        <li><span>Caesar Salad</span><span>$4.95</span></li>
        <li><span>Gyro Salad</span><span>$5.95</span></li>
        <li><span>Shrimp Caesar Salad</span><span>$6.25</span></li>
        <li><span>Greek Salad</span><span>$5.95</span></li>
      </ul>
      <span class="section-tag" style="right:0;top:172px;border-radius:9px 0 0 9px">GYRO &amp; SUBS</span>
      <ul class="price-list" style="left:250px;top:194px;width:262px">
        <li><span>Gyro (Original or Chicken)</span><span>$6.99</span></li>
        <li><span>¼ lb. Black Angus Burger</span><span>$3.99</span></li>
        <li><span>Buffalo Chicken Sandwich</span><span>$5.99</span></li>
        <li class="note"><span>YOUR CHOICE OF 6" OR FOOTLONG SUBS</span></li>
        <li><span>Po Boy Shrimp</span><span>$7.55-$9.25</span></li>
        <li><span>Philly (Steak or Chicken)</span><span>$6.75-$8.99</span></li>
        <li><span>Fish</span><span>$6.75-$8.99</span></li>
        <li><span>Turkey &amp; Cheese</span><span>$6.49-$7.95</span></li>
      </ul>
    </div>
  </div>
  <div class="panel panel--bottom">
    <div class="panel__inner">
      <span class="section-tag" style="left:0;top:14px">SIDES</span>
      <ul class="price-list" style="left:18px;top:36px;width:180px">
        <li><span>French Fries</span><span>$2.79</span></li>
        <li><span>Cajun Fries</span><span>$3.99</span></li>
        <li><span>Onion Rings</span><span>$4.99</span></li>
        <li><span>5 Jalapeno Poppers</span><span>$4.99</span></li>
        <li><span>Fried Okra</span><span>$4.99</span></li>
        <li><span>Fried Mushroom</span><span>$5.49</span></li>
        <li><span>5 Mozzarella Sticks</span><span>$5.49</span></li>
      </ul>

      <span class="section-tag" style="right:0;top:14px;border-radius:9px 0 0 9px">COMBOS <small style="font-size:7.5px">INCLUDES 16OZ SOFT DRINK!</small></span>
      <ul class="price-list" style="left:222px;top:36px;width:290px">
        <li><span>½ lb. Fish &amp; Fries</span><span>$9.99</span></li>
        <li><span>½ lb. Shrimp &amp; Fries</span><span>$10.99</span></li>
        <li><span>6" Philly (Steak or Chicken) &amp; Fries</span><span>$9.99</span></li>
        <li><span>Gyro (Original, Chicken or Fish) &amp; Fries</span><span>$9.49</span></li>
        <li><span>5 Wings &amp; Fries</span><span>$9.49</span></li>
        <li><span>½ lb. Gizzards &amp; Fries</span><span>$7.99</span></li>
        <li><span>¼ lb. Black Angus Burger &amp; Fries</span><span>$6.99 <em class="cheese">*cheese extra</em></span></li>
        <li><span>5 Wings &amp; Gizzards</span><span>$11.49</span></li>
        <li><span>½ lb. Chicken Strips &amp; Fries</span><span>$7.99</span></li>
      </ul>

      <div class="placeholder meal-photo" style="left:12px" role="img" aria-label="Photo of nuggets, burger, fries and a soda cup"></div>
      <div class="kids">
        <span class="section-tag">KIDS MEAL</span>
        <ul>
          <li><span>Chicken Nuggets 4pc with small drink &amp; fries</span><b>$4.95</b></li>
          <li><span>Chicken Strips 2pc with small drink &amp; fries</span><b>$4.95</b></li>
          <li><span>Mac &amp; Cheese</span><b>$3.95</b></li>
        </ul>
      </div>
      <div class="placeholder meal-photo" style="right:12px" role="img" aria-label="Photo of chicken tenders, fries and a soda cup"></div>
    </div>
  </div>
</section>

</body>
</html>
```